Shine4all

Full service cleaning company. Specializing in commercial and apartment cleans.
Fully licensed and insured
Digital photos and invoices provided
for every job
For web designer...basic info as expected by a highend cleaning company that provides excellent service at reasonable pricing. We are going after large property management companies as well as not pricing ourselves out to help the local mom and pop companies as well.

Project Deadline Extended Reason: Everyone seems to be having trouble understanding that we are a dumpster company that is adding a cleaning side to the company. We want our clients to see Shine4All as a separate branch of our our already established waste management company.We are not a regular cleaning company. We specialize in going after large commercial cleans and apartment cleans. I have now included info regarding a proposal for work and our invoice/job completion to make it clearer what we do Added Monday, July 20, 2015

Target Market(s)

Property Management companies in Savannah, Richmond Hill, Rincon, Hinesville and Midway Georgia

Industry/Entity Type

Cleaning Service

Coding

Coded - Design and coding required

Number of Pages Required

3 page

Requirements
Must have
• Nice home page with lots of photos (stock are fine) to convey exactly what we do (getting logo bid on right now on this sight).
• Information page with employee photos (can leave blank) need room for 4 photos and bios.
• Page or link to a static page for the dumpster company BinLoop (logo for this is red and black file attached along with photo of dumpster. This page just needs to be one page with contact info and information about commercial dumpster.
• Basically this site is just a fluff page used for marketing purposes. Its content can be general and once created wont change much. Services and photos can be provided upon request but general layout and info is what we are looking for.

```html
<!DOCTYPE html>
<html lang="en">
<head>
<meta charset="utf-8">
<title>Shine4All — Commercial &amp; Apartment Cleaning</title>
<link href="https://fonts.googleapis.com/css2?family=Open+Sans:ital,wght@0,400;0,600;0,700;0,800;1,400&family=Kaushan+Script&display=swap" rel="stylesheet">
<style>
:root{
  --red:#c8141c;
  --red-dark:#8e0d12;
  --ink:#1b1b1b;
  --black:#0e0e0e;
  --charcoal:#2a2a2a;
  --grey:#e6e6e6;
  --grey-mid:#b9b9b9;
  --text:#555;
  --white:#fff;
}
*{box-sizing:border-box;margin:0;padding:0}
html,body{width:1200px;height:2436px;overflow:hidden}
body{font-family:"Open Sans",Arial,sans-serif;color:var(--text);background:var(--white);font-size:14px;line-height:1.5;position:relative}
.script{font-family:"Kaushan Script",cursive}
.btn{display:inline-block;background:var(--charcoal);color:var(--white);font-weight:700;font-size:13px;letter-spacing:1px;padding:10px 34px;border-bottom:3px solid var(--red)}
.btn-red{background:var(--red);border-bottom:3px solid var(--red-dark)}

/* header */
.site-header{position:absolute;top:0;left:0;width:1200px;height:120px;background:linear-gradient(#1a1a1a,#050505)}
.logo{position:absolute;left:40px;top:28px;display:flex;align-items:center;gap:12px}
.logo-mark{width:26px;height:26px;background:var(--red)}
.logo-name{font-size:40px;font-weight:800;color:var(--white);line-height:1}
.logo-tag{position:absolute;left:40px;top:78px;font-size:11px;color:#aaa;letter-spacing:.5px}
.header-call{position:absolute;right:40px;top:30px;text-align:right;color:var(--white);font-size:12px;font-weight:700;line-height:1.9}
.header-call .phone{color:var(--red)}
.main-nav{position:absolute;top:120px;left:0;width:1200px;height:40px;background:linear-gradient(#3a3a3a,#1e1e1e);border-top:2px solid var(--red)}
.main-nav ul{list-style:none;display:flex;margin-left:120px}
.main-nav li{color:var(--white);font-size:12px;font-weight:700;padding:0 26px;line-height:38px}
.main-nav li.active{background:var(--red)}
.search{position:absolute;right:40px;top:8px;width:200px;height:24px;background:#111;border:1px solid #444;color:#777;font-size:11px;padding:3px 10px}
.search svg{position:absolute;right:6px;top:4px}

/* hero */
.hero{position:absolute;top:160px;left:0;width:1200px;height:590px;background:radial-gradient(circle at 30% 40%,#3b3b3b,#0a0a0a 75%)}
.hero-slide{position:absolute;left:60px;top:20px;width:1080px;height:520px;overflow:hidden}
.hero-photo{position:absolute;inset:0;background:linear-gradient(90deg,#f3f0ea 0%,#d9d2c6 45%,#ece7de 70%,#f6f4f0 100%)}
.hero-person{position:absolute;right:60px;top:0;width:330px;height:520px;background:linear-gradient(#2b2b2b,#151515)}
.hero-copy{position:absolute;left:60px;top:90px;width:560px}
.hero-copy .lead{font-size:40px;font-weight:600;color:var(--ink);line-height:1.1}
.hero-copy h1{font-size:70px;font-weight:700;color:var(--ink);line-height:1.05;margin-top:4px}
.hero-copy p{font-size:13px;color:#444;margin:8px 0 18px;width:420px}
.slider-dots{position:absolute;left:0;bottom:22px;width:1200px;display:flex;justify-content:center;gap:10px}
.slider-dots span{width:80px;height:5px;background:#555}
.slider-dots span.on{background:var(--red)}

/* services */
.services{position:absolute;top:780px;left:0;width:1200px;height:440px;display:flex;justify-content:center;gap:60px}
.service{width:340px;text-align:center}
.service-icon{width:130px;height:130px;margin:0 auto 20px;background:radial-gradient(circle,#e33a3a 0%,#b51017 60%,transparent 62%)}
.service h2{font-size:38px;font-weight:400;color:var(--ink)}
.service .price{color:var(--red);font-weight:800;font-size:24px;margin:4px 0}
.service p{font-size:12px;color:#777;margin-bottom:22px}
.service .quote-by{color:var(--red);font-weight:700;font-size:13px;margin:-14px 0 22px}

/* welcome */
.welcome{position:absolute;top:1250px;left:0;width:1200px;height:490px;background:var(--grey)}
.welcome-main{position:absolute;left:140px;top:60px;width:580px}
.welcome-main h2{font-size:40px;font-weight:400;color:var(--ink);margin-bottom:14px}
.welcome-main .intro{font-size:12px;font-weight:700;color:#444;text-transform:uppercase;margin-bottom:18px}
.welcome-cols{display:flex;gap:30px}
.welcome-cols .col{width:275px;font-size:12px}
.welcome-art{width:240px;height:120px;background:linear-gradient(#3a3a3a,#111);margin-bottom:14px}
.binloop-card{position:absolute;left:770px;top:60px;width:290px;height:390px;background:var(--white);text-align:center;padding-top:26px}
.binloop-card h3{font-size:20px;font-weight:800;color:var(--ink);letter-spacing:1px}
.binloop-card .bin-icon{margin:60px auto 0}
.binloop-photo{width:220px;height:100px;margin:50px auto 0;background:linear-gradient(#f0f0f0,#d6d6d6)}

/* cta */
.cta{position:absolute;top:1760px;left:0;width:1200px;height:76px;background:var(--red);display:flex;align-items:center;justify-content:center;gap:26px}
.cta p{color:var(--white);font-size:18px;font-weight:700;letter-spacing:.5px}
.cta .btn{background:var(--ink);border:none;padding:8px 22px}

/* contact & efficiency */
.info{position:absolute;top:1836px;left:0;width:1200px;height:520px;background:#fafafa}
.contact{position:absolute;left:150px;top:50px;width:360px}
.info h2{font-size:40px;font-weight:400;color:var(--ink);margin-bottom:16px}
.contact dl{font-size:13px;line-height:2}
.contact dt{display:inline;font-weight:700;color:var(--ink)}
.contact dd{display:inline}
.social{display:flex;gap:10px;margin:6px 0 16px}
.social span{width:26px;height:26px;border-radius:50%;background:#999}
.contact label{display:block;font-weight:700;color:var(--ink);font-size:13px;margin-bottom:6px}
.select-row{display:flex;gap:6px}
.select{width:200px;height:30px;border:1px solid #bbb;background:var(--white);font-size:12px;padding:5px 10px;color:#777}
.select-row .btn{padding:6px 12px;font-size:11px;border:none;background:var(--ink)}
.efficiency{position:absolute;left:580px;top:50px;width:480px}
.bar{margin-bottom:24px}
.bar-label{display:flex;justify-content:space-between;align-items:baseline}
.bar-label strong{font-size:20px;color:var(--ink);font-weight:700}
.bar-label small{font-size:11px;color:#888;margin-left:8px}
.bar-label em{font-style:normal;font-size:12px;color:#666}
.bar-track{height:8px;background:#ddd;margin-top:6px}
.bar-fill{height:8px;background:var(--red)}

/* footer */
.site-footer{position:absolute;top:2356px;left:0;width:1200px;height:80px;background:linear-gradient(#2a2a2a,#0c0c0c);display:flex;align-items:center;justify-content:space-between;padding:0 150px}
.site-footer ul{list-style:none;display:flex;gap:28px}
.site-footer li{color:var(--white);font-size:12px;font-weight:700}
.site-footer p{color:#aaa;font-size:12px}
</style>
</head>
<body>

<header class="site-header">
  <div class="logo"><span class="logo-mark"></span><span class="logo-name">Shine4All</span></div>
  <div class="logo-tag">Commercial &amp; apartment cleaning</div>
  <div class="header-call">
    CALL TO SCHEDULE YOUR FREE<br>
    NO OBLIGATION ASSESSMENT <span class="phone">+1 555 014 2890</span>
  </div>
</header>

<nav class="main-nav">
  <ul>
    <li class="active">HOME</li>
    <li>THE COMPANY</li>
    <li>SERVICES</li>
    <li>TESTIMONIALS</li>
    <li>CONTACT US</li>
    <li>BINLOOP</li>
  </ul>
  <div class="search">Search
    <svg width="14" height="14" viewBox="0 0 14 14"><circle cx="6" cy="6" r="4" fill="none" stroke="#ccc" stroke-width="2"/><line x1="9" y1="9" x2="13" y2="13" stroke="#ccc" stroke-width="2"/></svg>
  </div>
</nav>

<section class="hero">
  <div class="hero-slide">
    <div class="hero-photo" role="img" aria-label="Clean apartment hallway with a professional vacuum cleaner on the carpet"></div>
    <div class="hero-person" role="img" aria-label="Cleaning company representative holding a clipboard"></div>
    <div class="hero-copy">
      <div class="lead">We use only professional</div>
      <h1>Vacuum Cleaner</h1>
      <p>Commercial grade equipment on every job, for spotless common areas, offices and apartment units.</p>
      <span class="btn btn-red">SEE MORE</span>
    </div>
  </div>
  <div class="slider-dots"><span class="on"></span><span></span><span></span></div>
</section>

<section class="services">
  <article class="service">
    <div class="service-icon" role="img" aria-label="Red spray bottle icon"></div>
    <h2 class="script">Monthly Service</h2>
    <div class="price">$99/month</div>
    <p>Regular scheduled cleans for offices and<br>apartment complexes, every single month.</p>
    <span class="btn">LEARN MORE</span>
  </article>
  <article class="service">
    <div class="service-icon" role="img" aria-label="Red scrubbing brush icon"></div>
    <h2 class="script">Testimonials</h2>
    <p>"Reliable crew, photos after every job and<br>fair pricing. Our tenants noticed at once."</p>
    <div class="quote-by">Morgan Ellison</div>
    <span class="btn">FULL LIST</span>
  </article>
  <article class="service">
    <div class="service-icon" role="img" aria-label="Red cleaning bucket icon"></div>
    <h2 class="script">One Time Service</h2>
    <div class="price">$49/once</div>
    <p>Move-out and turnover cleans booked once,<br>with digital invoice on job completion.</p>
    <span class="btn">LEARN MORE</span>
  </article>
</section>

<section class="welcome">
  <div class="welcome-main">
    <h2 class="script">Welcome to Shine4All</h2>
    <p class="intro">A full service cleaning branch of an established waste company, built for property managers across coastal Georgia.</p>
    <div class="welcome-cols">
      <div class="col">
        <div class="welcome-art" role="img" aria-label="Illustration of a cleaning service calendar"></div>
        <p>We specialize in large commercial cleans and apartment turnovers, fully licensed and insured, with digital photos for every job.</p>
      </div>
      <div class="col">
        <p>From single units to entire complexes, our crews arrive on time and leave every space ready for the next tenant. Proposals are clear, prices fair, and each job closes with a photo report and invoice.</p>
        <p style="margin-top:12px">Large management firms and local family businesses get the same care, the same standards and the same honest rates.</p>
      </div>
    </div>
  </div>
  <aside class="binloop-card">
    <h3>BINLOOP</h3>
    <svg class="bin-icon" width="40" height="46" viewBox="0 0 40 46"><rect x="4" y="10" width="32" height="34" fill="#ccc"/><rect x="0" y="4" width="40" height="5" fill="#ccc"/><rect x="14" y="0" width="12" height="4" fill="#ccc"/></svg>
    <div class="binloop-photo" role="img" aria-label="Red commercial dumpster"></div>
  </aside>
</section>

<section class="cta">
  <p>IF YOU LIKE THIS, REQUEST A FREE QUOTE.</p>
  <span class="btn">GO</span>
</section>

<section class="info">
  <div class="contact">
    <h2 class="script">Contact Info</h2>
    <dl>
      <dt>Address:</dt> <dd>118 Harbor Lane, Savannah, GA 31401</dd><br>
      <dt>Telephone:</dt> <dd>+1 555 014 2890</dd><br>
      <dt>E-mail:</dt> <dd>hello@shine4all.example</dd>
    </dl>
    <label style="margin-top:14px">Follow us:</label>
    <div class="social"><span></span><span></span><span></span></div>
    <label>Keep in touch with us:</label>
    <div class="select-row"><div class="select">E-mail</div><span class="btn">GO</span></div>
  </div>
  <div class="efficiency">
    <h2 class="script">Efficiency</h2>
    <div class="bar"><div class="bar-label"><span><strong>Pro Vacuum</strong><small>Cleaning Efficiency</small></span><em>93%</em></div><div class="bar-track"><div class="bar-fill" style="width:93%"></div></div></div>
    <div class="bar"><div class="bar-label"><span><strong>Home Vacuum</strong><small>Cleaning Efficiency</small></span><em>57%</em></div><div class="bar-track"><div class="bar-fill" style="width:57%"></div></div></div>
    <div class="bar"><div class="bar-label"><span><strong>Pro Steam Cleaner</strong><small>Energy Efficiency</small></span><em>87%</em></div><div class="bar-track"><div class="bar-fill" style="width:87%"></div></div></div>
    <div class="bar"><div class="bar-label"><span><strong>Home Steam Cleaner</strong><small>Energy Efficiency</small></span><em>60%</em></div><div class="bar-track"><div class="bar-fill" style="width:60%"></div></div></div>
  </div>
</section>

<footer class="site-footer">
  <ul><li>HOME</li><li>ABOUT</li><li>INSTALLATION</li><li>CONTACT</li></ul>
  <p>Copyright © 2015 Shine4All</p>
</footer>

</body>
</html>
```